letter head for a construction company

Company Name: Kalvani Construction Limited

Address: Pembeni Street, Tundavu Beach, Dar es salaam, Tanzania

Phone: 0738264159

email : info@kalvaniconstruction.com

website : www.kalvaniconstruction.com

```html
<!DOCTYPE html>
<html lang="en">
<head>
<meta charset="utf-8">
<title>Kalvani Construction Limited – Letterhead</title>
<link href="https://fonts.googleapis.com/css2?family=Roboto:wght@300;400;500;700&display=swap" rel="stylesheet">
<style>
  :root {
    --backdrop: #9c9ea6;
    --paper: #ffffff;
    --ink: #3a3a3c;
    --ink-soft: #4a4a4c;
    --charcoal: #4b4b4d;
    --orange: #ff8207;
    --rule: #c8c8c8;
    --sign-fill: #ececee;
  }
  * { margin: 0; padding: 0; box-sizing: border-box; }
  html, body {
    width: 1200px; height: 1179px; overflow: hidden;
    background: var(--backdrop);
    font-family: "Roboto", Arial, sans-serif;
  }
  .letterhead {
    position: absolute; left: 182px; top: 0;
    width: 835px; height: 1179px;
    background: var(--paper);
    overflow: hidden;
    color: var(--ink);
  }
  .corner-art {
    position: absolute; left: 631px; top: 0;
    width: 204px; height: 205px;
    background: linear-gradient(135deg, var(--orange) 0%, var(--charcoal) 100%);
  }
  .brand {
    position: absolute; left: 72px; top: 106px;
    font-weight: 700; color: var(--charcoal);
    line-height: 1;
  }
  .brand__name { display: block; font-size: 40px; letter-spacing: 1px; }
  .brand__sub { display: block; font-size: 14.5px; letter-spacing: 4.6px; margin-top: 6px; }
  .recipient {
    position: absolute; left: 77px; top: 339px;
    font-size: 11.7px; font-weight: 300; line-height: 14.9px; font-style: normal;
  }
  .letter-body {
    position: absolute; left: 77px; top: 465px; width: 686px;
    font-size: 12.3px; font-weight: 300; line-height: 14.9px;
    text-align: justify; letter-spacing: -0.1px;
  }
  .salutation { font-weight: 500; margin-bottom: 14.8px; }
  .letter-body p { margin-bottom: 14.8px; }
  .closing {
    position: absolute; left: 77px; top: 841px;
    font-size: 11.7px; font-weight: 300;
  }
  .signature {
    position: absolute; left: 73px; top: 870px;
    width: 138px; height: 57px;
    background: var(--sign-fill); border-radius: 4px;
  }
  .signatory {
    position: absolute; left: 77px; top: 945px;
    font-size: 11.7px; line-height: 14.9px; font-weight: 300;
  }
  .signatory strong { font-weight: 500; display: block; }
  .footer-rule {
    position: absolute; left: 72px; top: 1090px; width: 691px;
    height: 1px; background: var(--rule);
  }
  .footer-accent {
    position: absolute; left: 583px; top: 1086px; width: 180px;
    height: 4px; background: var(--orange);
  }
  .footer-contact {
    position: absolute; left: 72px; top: 1105px;
    font-size: 10px; line-height: 13.3px; color: var(--ink-soft);
  }
  .footer-contact .label { color: var(--orange); font-weight: 500; }
  .footer-web {
    position: absolute; right: 72px; top: 1105px;
    font-size: 10.5px; color: var(--ink-soft);
  }
  .footer-web .domain { color: var(--orange); font-weight: 500; }
</style>
</head>
<body>
<main class="letterhead">
  <div class="corner-art" role="img" aria-label="Decorative corner artwork in orange and charcoal"></div>

  <div class="brand">
    <span class="brand__name">KALVANI</span>
    <span class="brand__sub">CONSTRUCTION LIMITED</span>
  </div>

  <address class="recipient">
    Mr. Lucien Marwell<br>
    President and CEO<br>
    Veridane Labs LLC.<br>
    2180 Harlow Avenue, Suite 3100<br>
    Brookfield, NY 10127
  </address>

  <section class="letter-body">
    <p class="salutation">Dear Mr. Marwell:</p>
    <p>As Chairperson of the Corporate Conscience Campaign - Helping the Homeless in New York, I am writing this to thank you personally for your company's support in last month's fund-raising effort.</p>
    <p>As I indicated when we spoke on the phone two weeks ago, the campaign was considered a resounding success, raising a total of $1.65 million to-date, significantly exceeding our target of $1 million. Some donations are still trickling in, so we could end up close to a total of $2 million.</p>
    <p>Veridane Labs was an influential leader throughout the entire three-month campaign. In fact, we couldn't have succeeded without the generous support of your company, both financially, and through your organizational and administrative assistance. Your Team Leader, Marisol Trenton was particularly impressive, going above and beyond what we could have expected of someone performing as a volunteer while continuing on with her day-to-day duties. Please convey my special thanks to Marisol.</p>
    <p>I would also ask you to convey my sincere thanks and congratulations to all of those other people in your company who contributed in any way to the Helping the Homeless Campaign. Please tell them that the sum of their contributions resulted in a major success that they should all be proud of taking part in.</p>
    <p>I believe that the 27 companies that participated in this effort have set a new standard for social responsibility in this community, and have set a powerful example that will inspire other companies and organizations to do the same.</p>
    <p>I look forward to seeing you at the Mayor's special thank you reception next month.</p>
  </section>

  <p class="closing">Yours sincerely,</p>
  <div class="signature" role="img" aria-label="Handwritten signature of Desmond Achterberg"></div>
  <p class="signatory"><strong>Desmond Achterberg</strong>Fundraising Chair</p>

  <div class="footer-rule"></div>
  <div class="footer-accent"></div>
  <div class="footer-contact">
    Pembeni Street, Tundavu Beach, Dar es salaam, Tanzania<br>
    <span class="label">T:</span> 0738264159 · <span class="label">E:</span> info@kalvaniconstruction.com
  </div>
  <div class="footer-web"><span class="domain">KALVANICONSTRUCTION</span>.COM</div>
</main>
</body>
</html>
```